Bookkeeping business needs a digital and print flyer

We need a flyer to promote our virtual bookkeeping services to small and mid-sized businesses in the United States. We want the content and design of the flyer to be consistent with our website: www.brightlanebookkeeping.example. We would like both a print version and a digital version of the flyer.

```html
<!DOCTYPE html>
<html lang="en">
<head>
<meta charset="utf-8">
<title>Bright Lane Bookkeeping – Virtual Bookkeeping Flyer</title>
<link rel="stylesheet" href="https://fonts.googleapis.com/css2?family=Fira+Sans+Condensed:wght@700;800&family=Montserrat:wght@300&family=Questrial&family=Tinos:wght@700&display=swap">
<style>
  :root {
    --ink-dark: #211b19;
    --brand-yellow: #f5c102;
    --paper-white: #ffffff;
    --ring-grey: #a9a9a9;
    --photo-light: #eef0ee;
    --photo-mid: #d9dcd8;
  }
  * { margin: 0; padding: 0; box-sizing: border-box; }
  html, body {
    width: 1200px;
    height: 1200px;
    overflow: hidden;
    background: var(--ink-dark);
  }
  .flyer {
    position: relative;
    width: 1200px;
    height: 1200px;
    background: var(--ink-dark);
    color: var(--paper-white);
    overflow: hidden;
  }

  /* Brand name block */
  .brand {
    position: absolute;
    top: 66px;
    right: 213px;
    text-align: right;
    font-family: "Montserrat", sans-serif;
    font-weight: 300;
    color: var(--paper-white);
    line-height: 1;
  }
  .brand-name { font-size: 62px; letter-spacing: 1px; white-space: nowrap; }
  .brand-sub { font-size: 29px; letter-spacing: 2px; margin-top: 12px; }
  .brand-dot {
    position: absolute;
    top: 70px;
    left: 1018px;
    width: 116px;
    height: 116px;
    border: 4px solid var(--paper-white);
    border-radius: 50%;
  }

  /* Headline */
  .headline {
    position: absolute;
    left: 82px;
    font-family: "Fira Sans Condensed", sans-serif;
    font-weight: 800;
    line-height: 1;
    white-space: nowrap;
  }
  .headline-top { top: 180px; font-size: 112px; color: var(--paper-white); }
  .headline-main { top: 270px; font-size: 174px; color: var(--brand-yellow); letter-spacing: -1px; }
  .headline-bottom { top: 440px; font-size: 112px; color: var(--paper-white); }

  /* Body copy */
  .copy {
    position: absolute;
    left: 149px;
    top: 585px;
    font-family: "Tinos", serif;
    font-weight: 700;
    font-size: 26px;
    line-height: 30.7px;
    color: var(--paper-white);
  }
  .copy p { margin-bottom: 30.7px; }
  .benefits { list-style: none; }

  /* Portrait */
  .portrait {
    position: absolute;
    left: 822px;
    top: 488px;
    width: 510px;
    height: 510px;
  }

  /* Call to action */
  .cta-line {
    position: absolute;
    left: 95px;
    top: 1008px;
    width: 1050px;
    font-family: "Fira Sans Condensed", sans-serif;
    font-weight: 700;
    font-size: 40px;
    letter-spacing: 0.3px;
    color: var(--paper-white);
    white-space: nowrap;
  }
  .call-pill {
    position: absolute;
    left: 203px;
    top: 1072px;
    width: 769px;
    height: 82px;
    border-radius: 41px;
    background: var(--brand-yellow);
    color: var(--ink-dark);
    font-family: "Questrial", sans-serif;
    font-size: 62px;
    line-height: 82px;
    text-align: center;
    letter-spacing: 1px;
    white-space: nowrap;
  }
</style>
</head>
<body>
<main class="flyer">
  <header class="brand">
    <div class="brand-name">BRIGHT LANE</div>
    <div class="brand-sub">BOOKKEEPING</div>
  </header>
  <div class="brand-dot" aria-hidden="true"></div>

  <h1>
    <span class="headline headline-top">Virtual</span>
    <span class="headline headline-main">Bookkeeping</span>
    <span class="headline headline-bottom">for Small Business</span>
  </h1>

  <section class="copy">
    <p>Take charge of your business and concentrate on your<br>strengths to become its hero!<br>Outsource your bookkeeping!</p>
    <ul class="benefits">
      <li>Take back your time</li>
      <li>Do more of what you love</li>
      <li>Focus on your strengths and what you do best</li>
      <li>Confidently make business decisions</li>
      <li>Sail through tax time</li>
      <li>Save over the expense of a full-time employee</li>
      <li>Pay yourself more</li>
      <li>Experience financial peace</li>
    </ul>
  </section>

  <svg class="portrait" viewBox="0 0 510 510" role="img" aria-label="Photo of a smiling businessman in a white shirt and tie, arms folded on a desk lined with small yellow rubber ducks">
    <defs>
      <linearGradient id="portraitTone" x1="0" y1="0" x2="0" y2="1">
        <stop offset="0" stop-color="var(--photo-light)"/>
        <stop offset="0.75" stop-color="var(--photo-mid)"/>
        <stop offset="1" stop-color="#e4e8e4"/>
      </linearGradient>
    </defs>
    <circle cx="255" cy="255" r="252" fill="var(--ring-grey)"/>
    <circle cx="255" cy="255" r="247" fill="url(#portraitTone)"/>
  </svg>

  <p class="cta-line">Set up a free consultation to see how you can take back your life.</p>
  <div class="call-pill">Call now 5550142876</div>
</main>
</body>
</html>
```